Health Clinic needs Stages of Osteoarthritis Infograph flyer

We are a knee clinic that specializes in non-surgical options for knee pain. Most of our treatments are for help with Osteoarthritis (OA).
We need a simplified easy to understand Infographic illustration handout of the OA grades and process of OA to give our patients as well as display digitally.
The final product should be divided into two pages/sections:
1) A Summary of information about OA
2) Unique Infographic illustration of knee joints at each grade of OA w/ short description of each grade.

A Summary of information about OA and a graphic representation of what we would like drawn is attached below to be incorporated into the flyer.

Also attached are also copies of current treatment handouts, these are to be used as examples of the style and design we want, none of the information is needed. Ideally, the handout would also incorporate our company color profile and use of the Museo Slab 300 font shown on each handout.

This is to be printed material as well as digital, so minimal photography and dark ink usage is encouraged.

Please see all attached files for more information on the process of OA.
This flyer should include unique visual graphics of a knee joint at each grade of OA.
You are also encouraged to visit our website: Kantevia.com to better understand what we do.
Thanks!

Industry/Entity Type

Health Care

Font styles to use
Other font styles liked:
• Museo Slab 300

Requirements
Must have
• Museo Slab 300 font
• Visual graphics of a knee joint and summary of grade at each grade/stage of OA
• company color profile

```html
<!DOCTYPE html>
<html lang="en">
<head>
<meta charset="utf-8">
<title>Kantevia – Summary of Osteoarthritis</title>
<link rel="stylesheet" href="https://fonts.googleapis.com/css2?family=Mulish:wght@300;400&family=Zilla+Slab:wght@300;700&display=swap">
<style>
  :root {
    --teal: #5bb8d4;
    --orange: #f7941d;
    --ink: #444444;
    --grey: #6d6d6d;
    --paper: #ffffff;
    --backdrop: #ecebe8;
  }
  * { box-sizing: border-box; margin: 0; padding: 0; }
  html, body { width: 1200px; height: 1200px; overflow: hidden; }
  body { background: var(--backdrop); font-family: "Mulish", sans-serif; color: var(--ink); }

  .flyer {
    position: absolute; left: 182px; top: 10px;
    width: 835px; height: 1180px;
    background: var(--paper); overflow: hidden;
  }
  .shapes { position: absolute; left: 0; top: 0; }

  .brand { position: absolute; left: 50px; top: 84px; width: 240px; text-align: center; }
  .brand-name { font-family: "Mulish", sans-serif; font-weight: 400; font-size: 54px; color: var(--teal); line-height: 1; }

  .summary-title {
    position: absolute; left: 47px; top: 215px;
    font-weight: 300; font-size: 36px; line-height: 37px; color: var(--teal);
  }
  .summary-list {
    position: absolute; left: 49px; top: 318px; width: 345px;
    list-style: none; font-size: 14.4px; line-height: 18.6px; font-weight: 300;
    text-align: justify;
  }
  .summary-list li { position: relative; padding-left: 22px; }
  .summary-list li::before {
    content: ""; position: absolute; left: 1px; top: 7px;
    width: 4px; height: 4px; border-radius: 50%; background: var(--teal);
  }

  .scale-title {
    position: absolute; left: 487px; top: 304px;
    font-family: "Zilla Slab", serif; font-weight: 300;
    font-size: 26px; line-height: 26px; color: var(--paper);
  }
  .grade-list { position: absolute; left: 489px; top: 379px; list-style: none; }
  .grade { display: flex; align-items: center; height: 62.5px; }
  .grade-num {
    flex: none; width: 47px; height: 47px; border-radius: 50%;
    background: var(--paper); color: var(--teal);
    display: flex; align-items: center; justify-content: center;
    font-weight: 300; font-size: 32px;
  }
  .grade-text {
    margin-left: 13px; width: 250px;
    font-size: 14.4px; line-height: 16px; font-weight: 300; color: var(--paper);
  }

  .stages-title {
    position: absolute; left: 330px; width: 452px; top: 768px; text-align: center;
    font-family: "Zilla Slab", serif; font-weight: 700; font-size: 20px; color: var(--teal);
    letter-spacing: 0.2px;
  }
  .stage { position: absolute; top: 803px; width: 118px; text-align: center; }
  .stage-label {
    font-family: "Zilla Slab", serif; font-weight: 700; font-size: 13px; line-height: 15px; color: #333;
  }
  .stage-art {
    margin: 6px auto 0; width: 106px; height: 207px; border-radius: 44px 44px 10px 10px;
  }
  .stage-note { margin-top: 5px; font-size: 6.6px; line-height: 7.6px; color: var(--grey); }

  .footer {
    position: absolute; left: 283px; top: 1083px; width: 552px; height: 97px;
    background: var(--orange); color: var(--paper);
    text-align: right; padding: 29px 47px 0 0;
    font-size: 13px; line-height: 18px; font-weight: 300;
  }
</style>
</head>
<body>
<main class="flyer">
  <svg class="shapes" width="835" height="1180" viewBox="0 0 835 1180">
    <defs>
      <linearGradient id="run-photo-tone" x1="0" y1="0" x2="0" y2="1">
        <stop offset="0" stop-color="#8a8c5a"/>
        <stop offset="0.3" stop-color="#5f6248"/>
        <stop offset="0.55" stop-color="#3a3a3d"/>
        <stop offset="1" stop-color="#5c5d60"/>
      </linearGradient>
      <linearGradient id="hands-photo-tone" x1="0" y1="0" x2="1" y2="1">
        <stop offset="0" stop-color="#f3f3f3"/>
        <stop offset="0.5" stop-color="#e9c4b4"/>
        <stop offset="1" stop-color="#f6eee9"/>
      </linearGradient>
    </defs>
    <path d="M442,236 Q470,258 560,282 L835,318 L835,730 L520,730 Q442,730 442,650 Z" fill="var(--orange)"/>
    <path role="img" aria-label="Photo of a runner sitting on a road holding a painful red-glowing knee"
          d="M472,0 L835,0 L835,303 L565,258 Q462,238 442,178 L442,125 Z" fill="url(#run-photo-tone)"/>
    <path role="img" aria-label="Photo of a doctor examining a patient's hand"
          d="M0,784 L232,834 Q302,850 306,905 L290,1180 L0,1180 Z" fill="url(#hands-photo-tone)"/>
  </svg>

  <header class="brand">
    <div class="brand-name">Kantevia</div>
  </header>

  <h1 class="summary-title">Summary<br>of Osteoarthritis (OA)</h1>
  <ul class="summary-list">
    <li>Osteoarthritis (OA) is a complex disease driven by inflammatory mediators released by cartilage, bone and synovium. This joint disease causes the cushion layer between one's bones, or cartilage to wear away. It begins with the inflammation, leading to gradual deterioration of cartilage. Without the protective cartilage, the bones begin to rub together, causing more inflammation, pain, loss of mobility, and eventual deformity.</li>
    <li>Symptoms can develop in a slow manner. They include, but are not limited to: pain, tenderness in the knee, stiffness when standing or walking, loss of flexibility, aching at night or while resting, and grating or grinding sensations that can be heard or felt when the knee joint is used.</li>
    <li>There is currently no cure for Osteoarthritis (OA). The treatments offered at Kantevia do not stop the progression of OA, rather significantly slow the progression. Patients with more advanced OA (grade 3-4) may require an increase in treatment frequency.</li>
  </ul>

  <h2 class="scale-title">Kellgren-Lawrence<br>Grading Scale of OA</h2>
  <ol class="grade-list">
    <li class="grade"><span class="grade-num">0</span><span class="grade-text">No radiographic features of osteoarthritis</span></li>
    <li class="grade"><span class="grade-num">1</span><span class="grade-text">Possible joint space narrowing, bone changes, sclerosis, and/or early osteophyte formation</span></li>
    <li class="grade"><span class="grade-num">2</span><span class="grade-text">Definite osteophyte formation with bone changes, sclerosis, and possible joint space narrowing</span></li>
    <li class="grade"><span class="grade-num">3</span><span class="grade-text">Multiple osteophytes, definite joint space narrowing, sclerosis and possible bony deformity</span></li>
    <li class="grade"><span class="grade-num">4</span><span class="grade-text">Large osteophytes, marked joint space narrowing, severe sclerosis and definite bony deformity</span></li>
  </ol>

  <h2 class="stages-title">STAGE OF KNEE OSTEOARTHRITIS</h2>
  <section class="stage" style="left:323px">
    <div class="stage-label">I<br>Doubtful</div>
    <div class="stage-art" role="img" aria-label="Illustration of a knee joint with minimal cartilage wear" style="background:linear-gradient(#f1c9a0,#a9d4ef 45%,#f1c9a0 60%,#e6b892)"></div>
    <p class="stage-note">Minimal change.<br>Early cartilage wear begins.</p>
  </section>
  <section class="stage" style="left:441px">
    <div class="stage-label">II<br>Mild</div>
    <div class="stage-art" role="img" aria-label="Illustration of a knee joint with mild joint space narrowing" style="background:linear-gradient(#f1c9a0,#a9d4ef 45%,#f1c9a0 60%,#e6b892)"></div>
    <p class="stage-note">Joint space narrows. Cartilage starts<br>to break down. Small spurs appear.</p>
  </section>
  <section class="stage" style="left:558px">
    <div class="stage-label">III<br>Moderate</div>
    <div class="stage-art" role="img" aria-label="Illustration of a knee joint with moderate cartilage gaps" style="background:linear-gradient(#f1c9a0,#a9d4ef 45%,#f1c9a0 60%,#e6b892)"></div>
    <p class="stage-note">Moderate space loss. Gaps in<br>cartilage widen toward the bone.</p>
  </section>
  <section class="stage" style="left:675px">
    <div class="stage-label">IV<br>Severe</div>
    <div class="stage-art" role="img" aria-label="Illustration of a knee joint with severe cartilage loss and large spurs" style="background:linear-gradient(#f1c9a0,#a9d4ef 42%,#f08c7a 50%,#f1c9a0 58%,#e6b892)"></div>
    <p class="stage-note">Joint space greatly reduced.<br>Most cartilage is lost. Large spurs.</p>
  </section>

  <footer class="footer">
    2 Alder Park 4810 NW Brookline Avenue, Suite 210, Salem, OR 97301<br>
    (555) 014-2290 &nbsp;|&nbsp; www.kantevia.com
  </footer>
</main>
</body>
</html>
```